Facebook & Instagram Ad Design for Chiropractor

I'd like a series of ads developed for our chiropractic office to use on Facebook and Instagram. I've attached the versions we're using today. They need to be updated. The offer content would be generally the same. There are two types of ads we're seeking. One for basic chiropractic services and the other for chiropractic decompression services.

Current ads can be seen in attached and here:
https://lnk.example/8TrQ2zXvPoLkm3A

Learn more about the company at www.bellwingchiropractic.example

Target Market(s)

Potential patients seeking chiropractic care or who are unaware that chiropractic could help them (suffer from back pain, etc.) in the greater Green Bay, WI area.

Industry/Entity Type

Chiropractic

Font styles to use
Sans Serif

Colors
0592cd
3277b5

Requirements
Must have
• Compelling visuals
Comply with text requirements for FB & Insta ads
Should not have
• Clinical images that depict traditional medical care

```html
<!DOCTYPE html>
<html lang="en">
<head>
<meta charset="utf-8">
<title>Bellwing Chiropractic – New Patient Offer Post</title>
<link rel="stylesheet" href="https://fonts.googleapis.com/css2?family=PT+Sans+Narrow:wght@700&family=Montserrat:wght@400;700&family=Arimo:wght@400;700&display=swap">
<style>
  :root {
    --page-bg: #ffffff;
    --card-border: #dddfe2;
    --divider: #e5e6e9;
    --page-name: #365899;
    --meta-grey: #616770;
    --action-grey: #606770;
    --placeholder: #90949c;
    --body-ink: #1d2129;
    --react-blue: #4a83f0;
    --avatar-navy: #0c0c4a;
    --photo-light: #ececec;
    --photo-mid: #d9d9d9;
    --photo-skin: #8a8a8a;
    --navy: #19243a;
    --brand-ink: #15233b;
    --accent-red: #a3162a;
    --white: #ffffff;
  }
  * { margin: 0; padding: 0; box-sizing: border-box; }
  html, body {
    width: 1053px;
    height: 1200px;
    overflow: hidden;
    background: var(--page-bg);
  }
  .canvas {
    position: relative;
    width: 1053px;
    height: 1200px;
    font-family: "Arimo", Arial, sans-serif;
  }
  .canvas__edge {
    position: absolute;
    left: 1046px;
    top: 0;
    width: 2px;
    height: 1200px;
    background: var(--divider);
  }
  .post {
    position: absolute;
    left: 22px;
    top: 21px;
    width: 999px;
    height: 1151px;
    border: 1px solid var(--card-border);
    border-radius: 4px;
    background: var(--white);
  }
  .post__avatar {
    position: absolute;
    left: 25px;
    top: 25px;
    width: 84px;
    height: 84px;
    border-radius: 50%;
    background: var(--avatar-navy);
  }
  .post__name {
    position: absolute;
    left: 127px;
    top: 33px;
    font-weight: 700;
    font-size: 28px;
    line-height: 32px;
    color: var(--page-name);
    white-space: nowrap;
  }
  .post__meta {
    position: absolute;
    left: 127px;
    top: 74px;
    display: flex;
    align-items: center;
    gap: 22px;
    font-size: 23px;
    line-height: 26px;
    color: var(--meta-grey);
  }
  .post__more {
    position: absolute;
    right: 18px;
    top: 35px;
  }
  .post__message {
    position: absolute;
    left: 25px;
    top: 155px;
    width: 900px;
    font-size: 28px;
    line-height: 39px;
    color: var(--body-ink);
  }

  .ad {
    position: absolute;
    left: -1px;
    top: 294px;
    width: 999px;
    height: 524px;
    overflow: hidden;
  }
  .ad__photo {
    position: absolute;
    inset: 0;
    background:
      radial-gradient(ellipse 250px 320px at 250px 290px, var(--photo-skin) 0%, rgba(138,138,138,0.35) 55%, rgba(138,138,138,0) 100%),
      linear-gradient(90deg, var(--photo-light) 0%, var(--photo-mid) 100%);
  }
  .ad__brand {
    position: absolute;
    right: 28px;
    top: 56px;
    font-family: "PT Sans Narrow", "Arial Narrow", sans-serif;
    font-weight: 700;
    font-size: 62px;
    line-height: 1;
    color: var(--brand-ink);
    white-space: nowrap;
    letter-spacing: -1px;
  }
  .ad__brand-rule {
    position: absolute;
    left: 536px;
    top: 123px;
    width: 438px;
    height: 2px;
    background: var(--accent-red);
  }
  .ad__band-edge {
    position: absolute;
    left: 0;
    top: 286px;
    width: 29px;
    height: 174px;
    background: var(--navy);
  }
  .ad__band {
    position: absolute;
    left: 449px;
    top: 286px;
    width: 524px;
    height: 174px;
    background: var(--navy);
    color: var(--white);
    font-family: "Montserrat", sans-serif;
  }
  .offer__line {
    position: absolute;
    right: 24px;
    line-height: 1;
    white-space: nowrap;
  }
  .offer__label { font-weight: 400; font-size: 35px; }
  .offer__label--top { top: 21px; }
  .offer__label--bottom { top: 121px; }
  .offer__price { top: 60px; font-weight: 700; font-size: 57px; letter-spacing: -1px; }

  .actions {
    position: absolute;
    left: 0;
    top: 900px;
    width: 997px;
    height: 60px;
  }
  .action {
    position: absolute;
    top: 8px;
    display: flex;
    align-items: center;
    gap: 12px;
    font-weight: 700;
    font-size: 27px;
    color: var(--action-grey);
  }
  .action--like { left: 113px; }
  .action--comment { left: 361px; }
  .action--share { left: 670px; }
  .actions__menu { position: absolute; left: 937px; top: 28px; }

  .post__divider {
    position: absolute;
    left: 0;
    width: 997px;
    height: 2px;
    background: var(--divider);
  }
  .post__divider--top { top: 961px; }
  .post__divider--bottom { top: 1043px; }

  .reactions {
    position: absolute;
    left: 25px;
    top: 985px;
    display: flex;
    align-items: center;
    gap: 7px;
    font-size: 23px;
    color: var(--page-name);
  }
  .reactions__dot {
    width: 34px;
    height: 34px;
    border-radius: 50%;
    background: var(--react-blue);
  }

  .composer__avatar {
    position: absolute;
    left: 25px;
    top: 1064px;
    width: 67px;
    height: 67px;
    border-radius: 50%;
    background: var(--avatar-navy);
  }
  .composer__field {
    position: absolute;
    left: 108px;
    top: 1062px;
    width: 863px;
    height: 69px;
    border: 1.5px solid var(--card-border);
    border-radius: 35px;
  }
  .composer__placeholder {
    position: absolute;
    left: 24px;
    top: 18px;
    font-size: 27px;
    line-height: 30px;
    color: var(--placeholder);
  }
  .composer__icons {
    position: absolute;
    right: 22px;
    top: 17px;
    display: flex;
    gap: 28px;
  }
</style>
</head>
<body>
  <div class="canvas">
    <div class="canvas__edge"></div>
    <article class="post">
      <header>
        <div class="post__avatar"></div>
        <h2 class="post__name">Bellwing Chiropractor, SC</h2>
        <div class="post__meta">
          <span>18 hrs</span>
          <svg width="26" height="26" viewBox="0 0 26 26" aria-hidden="true">
            <circle cx="13" cy="13" r="11" fill="none" stroke="#616770" stroke-width="2.5"/>
            <path d="M6 8c3 0 4 2 3 4s1 3 2 5M15 4c0 3 2 3 4 4s1 4 3 5" fill="none" stroke="#616770" stroke-width="2.5" stroke-linecap="round"/>
          </svg>
        </div>
        <svg class="post__more" width="36" height="10" viewBox="0 0 36 10" aria-hidden="true">
          <circle cx="5" cy="5" r="4.5" fill="#606770"/>
          <circle cx="18" cy="5" r="4.5" fill="#606770"/>
          <circle cx="31" cy="5" r="4.5" fill="#606770"/>
        </svg>
      </header>

      <p class="post__message">Your post message text goes in this area, you can edit it easily according to your needs, enjoy.</p>

      <section class="ad">
        <div class="ad__photo" role="img" aria-label="Black and white photo of a woman in white sportswear holding her lower back, with a red glow marking back pain"></div>
        <h1 class="ad__brand">Bellwing Chiropractic</h1>
        <div class="ad__brand-rule"></div>
        <div class="ad__band-edge"></div>
        <div class="ad__band">
          <span class="offer__line offer__label offer__label--top">NEW PATIENT</span>
          <span class="offer__line offer__price">$ 25</span>
          <span class="offer__line offer__label offer__label--bottom">OFFER</span>
        </div>
      </section>

      <nav class="actions">
        <span class="action action--like">
          <svg width="40" height="40" viewBox="0 0 40 40" aria-hidden="true">
            <path d="M3 18h8v19H3zM11 19l7-10c1-3 1-6 4-6 3 0 4 4 3 7l-2 6h11c2 0 4 2 3 4l-3 13c-1 2-2 3-4 3H11" fill="none" stroke="#606770" stroke-width="2.6" stroke-linejoin="round"/>
          </svg>Like</span>
        <span class="action action--comment">
          <svg width="38" height="38" viewBox="0 0 38 38" aria-hidden="true">
            <path d="M7 3h24c2 0 4 2 4 4v16c0 2-2 4-4 4H18l-8 8v-8H7c-2 0-4-2-4-4V7c0-2 2-4 4-4z" fill="none" stroke="#606770" stroke-width="2.6" stroke-linejoin="round"/>
          </svg>Comment</span>
        <span class="action action--share">
          <svg width="40" height="38" viewBox="0 0 40 38" aria-hidden="true">
            <path d="M24 3l13 13-13 13v-7C14 22 7 26 3 35c0-12 6-22 21-23z" fill="none" stroke="#606770" stroke-width="2.6" stroke-linejoin="round"/>
          </svg>Share</span>
        <svg class="actions__menu" width="20" height="12" viewBox="0 0 20 12" aria-hidden="true">
          <path d="M0 0h20L10 12z" fill="#606770"/>
        </svg>
      </nav>

      <div class="post__divider post__divider--top"></div>
      <div class="reactions">
        <span class="reactions__dot"></span>
        <span>82</span>
      </div>
      <div class="post__divider post__divider--bottom"></div>

      <div class="composer__avatar"></div>
      <div class="composer__field">
        <span class="composer__placeholder">Write a comment..</span>
        <div class="composer__icons" aria-hidden="true">
          <svg width="34" height="34" viewBox="0 0 34 34">
            <circle cx="17" cy="17" r="15" fill="none" stroke="#606770" stroke-width="2.2"/>
            <circle cx="12" cy="13" r="2" fill="#606770"/>
            <circle cx="22" cy="13" r="2" fill="#606770"/>
            <path d="M10 20c4 5 10 5 14 0" fill="none" stroke="#606770" stroke-width="2.2" stroke-linecap="round"/>
          </svg>
          <svg width="34" height="34" viewBox="0 0 34 34">
            <path d="M4 6c8-3 18-4 27-2 1 8 0 16-4 22l-8 6C11 31 6 28 4 22z" fill="none" stroke="#606770" stroke-width="2.2" stroke-linejoin="round"/>
            <circle cx="13" cy="14" r="2" fill="#606770"/>
            <circle cx="22" cy="13" r="2" fill="#606770"/>
          </svg>
        </div>
      </div>
    </article>
  </div>
</body>
</html>
```